Private Chef booking platform landing page design

I need an amazing design for a landing page for my upcoming private chef booking platform Platerva. You can view my current page here: www.platerva.co.uk/mainindex.php. The design on this page is wrong right now. This platform is in Beta and the main purpose is to sign up chefs. Similar to what Rydexa.com is doing with their website -> become a driver. In my case we should have a button that says "become a chef", state the benefits of becoming a chef such as earning extra money, managing your time and bookings, increasing your client base and be creative with your food menus at the same time. Also, somewhere on the website it needs to say that we are currently in Beta mode and sign up to help us grow. In terms of visuals, I want the design to be sleek and clean and also adaptable to mobile devices as I am using html5. You can also re-design the current logo and choose any colours you think would be suitable for such a concept. Similar concept websites: hobwanderly.com and stovlin.com
Updates

Target Market(s)

upper middle class

Industry/Entity Type

Chef

Number of Pages Required

1 page

Font styles to use
Sans Serif

Requirements
Must have
• see brief and check hobwanderly.com and stovlin.com for inspiration and also rydexa.com
Nice to have
• see brief
Should not have
• bad visuals

```html
<!DOCTYPE html>
<html lang="en">
<head>
<meta charset="utf-8">
<title>Platerva – Private chef bookings</title>
<link rel="stylesheet" href="https://fonts.googleapis.com/css2?family=Allura&family=Lobster&family=Fredoka:wght@600&family=Lato:wght@400;700&display=swap">
<style>
  :root {
    --orange: #d9540f;
    --charcoal: #333132;
    --paper: #efeeec;
    --white: #ffffff;
    --ink: #2b2a2a;
    --rule: #d6d4d1;
  }
  * { box-sizing: border-box; margin: 0; padding: 0; }
  html, body { width: 1174px; height: 1200px; overflow: hidden; }
  body { position: relative; background: var(--paper); font-family: "Lato", sans-serif; color: var(--ink); }
  a { text-decoration: none; }

  .topbar { position: absolute; left: 0; top: 0; width: 1174px; height: 39px; background: var(--white); z-index: 3; }
  .topnav { position: absolute; right: 59px; top: 7px; display: flex; gap: 18px; font-family: "Lobster", cursive; font-size: 19px; }
  .topnav a { color: var(--ink); }
  .topnav a.is-active { color: var(--orange); }

  .brand-wave { position: absolute; left: 0; top: 0; z-index: 4; }
  .brand { position: absolute; left: 52px; top: 52px; z-index: 5; display: flex; align-items: center; gap: 8px;
           font-family: "Lobster", cursive; font-size: 36px; color: var(--ink); }
  .brand-dot { width: 12px; height: 12px; border-radius: 50%; background: var(--orange); }

  .hero { position: absolute; left: 0; top: 39px; width: 1174px; height: 640px;
          background: linear-gradient(100deg, #6e6a66 0%, #8f8a85 35%, #a7a29c 60%, #7a746d 85%, #5c5650 100%); }
  .hero-shade { position: absolute; inset: 0; background: linear-gradient(180deg, rgba(40,36,34,.15), rgba(40,36,34,.35)); }

  .headline { position: absolute; left: 0; top: 226px; width: 1174px; text-align: center; color: var(--white); z-index: 2; font-weight: 400; }
  .headline .line-1 { display: block; font-family: "Allura", cursive; font-size: 96px; line-height: 1; }
  .headline .line-2 { display: block; font-family: "Lobster", cursive; font-size: 70px; line-height: 1; margin-top: -16px; }

  .cta { position: absolute; top: 498px; width: 358px; height: 61px; border: 2px solid var(--white);
         color: var(--white); font-family: "Fredoka", sans-serif; font-weight: 600; font-size: 23px;
         letter-spacing: 1px; text-transform: uppercase; display: flex; align-items: center; justify-content: center; z-index: 2; }
  .cta-become { left: 144px; background: var(--orange); }
  .cta-how { left: 673px; background: var(--charcoal); }
  .hero-mark { position: absolute; left: 548px; top: 527px; font-family: "Lobster", cursive; font-size: 20px; color: rgba(255,255,255,.85); z-index: 2; }

  .pill { position: absolute; top: 653px; width: 158px; height: 51px; border: 3px solid var(--white); border-radius: 9px;
          color: var(--white); font-family: "Lobster", cursive; font-size: 23px; display: flex; align-items: center; justify-content: center;
          box-shadow: 0 2px 4px rgba(0,0,0,.25); z-index: 2; }
  .pill-signup { left: 421px; background: var(--orange); }
  .pill-login { left: 595px; background: var(--charcoal); }

  .benefits-head { position: absolute; left: 0; top: 746px; width: 1174px; text-align: center; }
  .benefits-title { position: absolute; left: 452px; top: 24px; width: 272px; height: 46px; border: 1px solid var(--rule);
                    display: flex; align-items: center; justify-content: center; text-transform: uppercase;
                    font-family: "Fredoka", sans-serif; font-weight: 600; font-size: 23px; letter-spacing: 1px; color: var(--ink); }
  .star { position: absolute; top: 38px; }

  .benefit { position: absolute; top: 880px; width: 264px; text-align: center; }
  .benefit svg { display: block; margin: 0 auto; }
  .benefit p { margin-top: 22px; font-size: 17px; line-height: 1.2; color: var(--ink); }

  .footer { position: absolute; left: 0; top: 1092px; width: 1174px; height: 108px; background: var(--charcoal); color: var(--white); }
  .social { position: absolute; top: 30px; width: 100%; display: flex; justify-content: center; gap: 18px; font-size: 14px; text-transform: uppercase; }
  .social span { display: flex; align-items: center; gap: 6px; }
  .social i { width: 14px; height: 14px; background: var(--white); display: inline-block; }
  .copyright { position: absolute; top: 70px; width: 100%; text-align: center; font-size: 13px; font-weight: 700; letter-spacing: .3px; }
</style>
</head>
<body>

<header class="topbar">
  <nav class="topnav">
    <a href="#">Help</a>
    <a href="#">Sign Up</a>
    <a href="#" class="is-active">Login</a>
  </nav>
</header>

<svg class="brand-wave" width="380" height="150" viewBox="0 0 380 150" aria-hidden="true">
  <path d="M0 0 H380 V39 H350 C290 42 230 50 190 80 C150 112 120 140 80 134 C45 128 30 95 0 90 Z" fill="#ffffff"/>
  <path d="M350 39 C290 42 230 50 190 80 C150 112 120 140 80 134 C45 128 30 95 0 90" fill="none" stroke="#333132" stroke-width="3"/>
</svg>
<div class="brand"><span class="brand-dot"></span>Platerva</div>

<section class="hero" role="img" aria-label="Photo of a chef in white uniform preparing a dish with tomatoes and vegetables in a bright kitchen">
  <div class="hero-shade"></div>
</section>

<h1 class="headline">
  <span class="line-1">Chefs made meals</span>
  <span class="line-2">in your home</span>
</h1>

<a class="cta cta-become" href="#">Become a private chef</a>
<span class="hero-mark">Platerva</span>
<a class="cta cta-how" href="#">How it works on it</a>

<a class="pill pill-signup" href="#">Sign Up</a>
<a class="pill pill-login" href="#">Login</a>

<section class="benefits-head">
  <svg width="24" height="26" viewBox="0 0 24 26" style="display:block;margin:0 auto" aria-hidden="true">
    <path d="M6 16 C1 15 1 7 6 7 C7 2 17 2 18 7 C23 7 23 15 18 16 V23 H6 Z" fill="none" stroke="#d9540f" stroke-width="2"/>
    <line x1="6" y1="19" x2="18" y2="19" stroke="#d9540f" stroke-width="2"/>
  </svg>
  <svg class="star" style="left:420px" width="16" height="16" viewBox="0 0 16 16" aria-hidden="true"><path d="M8 1l2 5h5l-4 3 2 5-5-3-5 3 2-5-4-3h5z" fill="#c9c7c4"/></svg>
  <h2 class="benefits-title">For your benefits</h2>
  <svg class="star" style="left:739px" width="16" height="16" viewBox="0 0 16 16" aria-hidden="true"><path d="M8 1l2 5h5l-4 3 2 5-5-3-5 3 2-5-4-3h5z" fill="#c9c7c4"/></svg>
</section>

<div class="benefit" style="left:59px">
  <svg width="68" height="66" viewBox="0 0 68 66" aria-hidden="true">
    <g fill="#333132">
      <rect x="0" y="22" width="30" height="7" rx="2"/><rect x="0" y="31" width="30" height="7" rx="2"/>
      <rect x="0" y="40" width="30" height="7" rx="2"/><rect x="0" y="49" width="30" height="7" rx="2"/>
      <rect x="0" y="58" width="30" height="7" rx="2"/>
      <rect x="30" y="0" width="28" height="7" rx="2"/><rect x="30" y="9" width="28" height="7" rx="2"/>
      <circle cx="44" cy="42" r="23"/>
    </g>
    <circle cx="44" cy="42" r="17" fill="none" stroke="#efeeec" stroke-width="2.5"/>
    <text x="44" y="51" text-anchor="middle" font-family="Lato, sans-serif" font-weight="700" font-size="24" fill="#efeeec">$</text>
  </svg>
  <p>Earn extra money</p>
</div>

<div class="benefit" style="left:323px">
  <svg width="68" height="66" viewBox="0 0 68 66" aria-hidden="true">
    <rect x="2" y="8" width="54" height="50" rx="4" fill="#333132"/>
    <rect x="12" y="2" width="5" height="12" rx="2" fill="#333132"/><rect x="40" y="2" width="5" height="12" rx="2" fill="#333132"/>
    <g fill="#efeeec">
      <rect x="9" y="22" width="8" height="7"/><rect x="21" y="22" width="8" height="7"/><rect x="33" y="22" width="8" height="7"/>
      <rect x="9" y="33" width="8" height="7"/><rect x="21" y="33" width="8" height="7"/>
      <rect x="9" y="44" width="8" height="7"/><rect x="21" y="44" width="8" height="7"/>
    </g>
    <circle cx="52" cy="50" r="15" fill="#333132" stroke="#efeeec" stroke-width="3"/>
    <path d="M52 42 V50 H58" fill="none" stroke="#efeeec" stroke-width="2.5"/>
  </svg>
  <p>Fully manage your bookings<br>schedule</p>
</div>

<div class="benefit" style="left:587px">
  <svg width="68" height="66" viewBox="0 0 68 66" aria-hidden="true">
    <path d="M2 8 L34 14 L66 8 V56 L34 62 L2 56 Z" fill="#333132"/>
    <path d="M22 50 L44 22" stroke="#efeeec" stroke-width="3"/>
    <ellipse cx="46" cy="20" rx="5" ry="7" transform="rotate(38 46 20)" fill="#efeeec"/>
    <path d="M46 50 L24 22" stroke="#efeeec" stroke-width="3"/>
    <path d="M19 16 L23 26 M23 15 L26 24 M27 14 L28 22" stroke="#efeeec" stroke-width="2"/>
  </svg>
  <p>Be creative with your food menus</p>
</div>

<div class="benefit" style="left:852px">
  <svg width="68" height="66" viewBox="0 0 68 66" aria-hidden="true">
    <g fill="none" stroke="#333132" stroke-width="2.5">
      <circle cx="34" cy="14" r="12"/><circle cx="14" cy="50" r="12"/><circle cx="54" cy="50" r="12"/>
      <path d="M26 24 L20 39 M42 24 L48 39 M26 50 H42"/>
    </g>
    <g fill="#333132">
      <circle cx="34" cy="11" r="4"/><path d="M26 21 C27 15 41 15 42 21 Z"/>
      <circle cx="14" cy="47" r="4"/><path d="M6 57 C7 51 21 51 22 57 Z"/>
      <circle cx="54" cy="47" r="4"/><path d="M46 57 C47 51 61 51 62 57 Z"/>
    </g>
  </svg>
  <p>Expand your client base</p>
</div>

<footer class="footer">
  <div class="social">
    <span><i></i>Chatterly</span>
    <span><i></i>Friendfold</span>
    <span><i></i>Reelwave</span>
    <span><i></i>Circlenet</span>
    <span><i></i>Workweave</span>
  </div>
  <p class="copyright">© 2015 PLATERVA. ALL RIGHTS RESERVED.</p>
</footer>

</body>
</html>
```